Invitation Design Project

I would like to have a custom invitation (and reception/response cards) designed for my son's Bar Mitzvah. I have a strong idea of what I want and have a few mock-ups, but my "home made" effort would be improved by the addition of professional creativity and skill. The invitation should be white, red, and black, and a bold typographic style (see attachment). I am looking for a clean modern feel, and prefer square shaped invitations. I need the final product in an electronic format that I could either print myself or have done at a local printer.

Target Market(s)

Guests to a Bar Mitzvah. A group of family and friends ranging from 40-60 years of age, and a group of my son's 13 year old friends.

Industry/Entity Type

Electronic

Requirements
Must have
• Square shaped invitation (exact dimensions in attached file)
Typographic style
Red, black, white
Red color should be CMYK: 30-96-76-26
Nice to have
• I like the two icons on my attached sample reception card, especially the swirl/Torah one. I would be nice to use these (or similar ones) if there is a way to do so, but this is not a requirement.

```html
<!DOCTYPE html>
<html lang="en">
<head>
<meta charset="utf-8">
<title>Bar Mitzvah Invitation and Reply Card</title>
<link rel="stylesheet" href="https://fonts.googleapis.com/css2?family=PT+Sans+Narrow:wght@700&family=Source+Sans+3:wght@600;700&display=swap">
<style>
  :root {
    --paper: #ffffff;
    --ink: #111111;
    --grey: #a3a3a3;
    --grey-dark: #8e8e8e;
    --pink: #e79ca8;
    --rose: #b4606f;
    --mauve: #a8566a;
    --red: #c3102f;
    --red-deep: #861a2c;
    --frame: #3d3d3d;
    --line: #1a1a1a;
    --art: rgba(30, 30, 30, 0.08);
    --white: #ffffff;
  }
  html, body {
    margin: 0;
    padding: 0;
    overflow: hidden;
    background: var(--paper);
  }
  .canvas {
    width: 726px;
    height: 1200px;
    overflow: hidden;
    position: relative;
    background: var(--paper);
  }
  .canvas svg { display: block; }
  .reply-text {
    font-family: "Source Sans 3", "PT Sans", sans-serif;
    font-weight: 600;
    fill: var(--white);
    font-size: 23px;
  }
  .caption {
    font-family: "Source Sans 3", sans-serif;
    font-weight: 700;
    font-size: 19px;
    fill: var(--ink);
  }
  .invite-text {
    font-family: "Source Sans 3", sans-serif;
    font-weight: 600;
    fill: var(--white);
  }
  .invite-outline {
    font-family: "Source Sans 3", sans-serif;
    font-weight: 700;
    fill: none;
    stroke: var(--white);
    stroke-width: 2.2;
  }
  .hosts {
    font-family: "PT Sans Narrow", sans-serif;
    font-weight: 700;
    fill: var(--white);
    font-size: 38px;
  }
  .fill-grey { fill: var(--grey); }
  .fill-grey-dark { fill: var(--grey-dark); }
  .fill-pink { fill: var(--pink); }
  .fill-rose { fill: var(--rose); }
  .fill-mauve { fill: var(--mauve); }
  .fill-red { fill: var(--red); }
  .fill-red-deep { fill: var(--red-deep); }
  .art-area { fill: var(--art); }
  .rule { stroke: var(--line); stroke-width: 1.3; fill: none; }
  .write-line { stroke: var(--white); stroke-width: 1.2; }
  .card-frame { fill: none; stroke: var(--frame); stroke-width: 5; }
</style>
</head>
<body>
<div class="canvas">
<svg width="726" height="1200" viewBox="0 0 726 1200" xmlns="http://www.w3.org/2000/svg">

  <g class="reply-card">
    <rect class="fill-grey" x="56" y="15" width="609" height="422"/>
    <rect class="fill-pink" x="438" y="15" width="227" height="422"/>
    <rect class="fill-rose" x="438" y="15" width="23" height="422"/>
    <polyline class="rule" points="377,15 377,229 665,229"/>
    <rect class="art-area" x="93" y="127" width="51" height="292" role="img" aria-label="Line drawing of a fork"/>
    <rect class="art-area" x="185" y="95" width="320" height="330" role="img" aria-label="Line drawing of a dinner plate"/>
    <rect class="art-area" x="520" y="127" width="32" height="292" role="img" aria-label="Line drawing of a knife"/>

    <text class="reply-text" x="156" y="115" textLength="414" lengthAdjust="spacingAndGlyphs">The favor of a reply is requested by</text>
    <text class="reply-text" x="156" y="241">M</text>
    <line class="write-line" x1="178" y1="244" x2="566" y2="244"/>
    <line class="write-line" x1="152" y1="299" x2="207" y2="299"/>
    <text class="reply-text" x="212" y="296" textLength="261" lengthAdjust="spacingAndGlyphs">Accepts with pleasure</text>
    <line class="write-line" x1="152" y1="341" x2="207" y2="341"/>
    <text class="reply-text" x="212" y="338" textLength="240" lengthAdjust="spacingAndGlyphs">Declines with regret</text>
  </g>

  <text class="caption" x="371" y="470" text-anchor="middle">font above is meridian sans semi-bold</text>

  <g class="invitation">
    <rect class="fill-red" x="13" y="491" width="700" height="709"/>
    <rect class="fill-grey" x="35" y="514" width="603" height="293"/>
    <rect class="fill-pink" x="398" y="552" width="278" height="255"/>
    <rect class="fill-rose" x="366" y="552" width="32" height="255"/>
    <rect class="fill-mauve" x="35" y="807" width="294" height="106"/>
    <rect class="fill-grey" x="329" y="807" width="347" height="90"/>
    <rect class="fill-pink" x="35" y="913" width="252" height="265"/>
    <rect class="fill-grey-dark" x="287" y="897" width="414" height="281"/>
    <rect class="fill-red-deep" x="287" y="1178" width="425" height="22"/>
    <rect class="card-frame" x="58" y="552" width="600" height="605"/>

    <rect class="art-area" x="37" y="514" width="313" height="367" role="img" aria-label="Line drawing of a tree with spreading branches"/>
    <rect class="art-area" x="350" y="595" width="350" height="350" role="img" aria-label="Line drawing of a six-pointed star"/>
    <rect class="art-area" x="16" y="871" width="271" height="308" role="img" aria-label="Line drawing of a fork and plate"/>

    <text class="invite-text" x="58" y="554" font-size="29" textLength="611" lengthAdjust="spacingAndGlyphs">IT IS WITH GREAT PRIDE AND JOY THAT</text>
    <text class="invite-text" x="58" y="597" font-size="29" textLength="611" lengthAdjust="spacingAndGlyphs">WE INVITE YOU TO JOIN US AS OUR SON</text>
    <text class="invite-outline" x="58" y="680" font-size="82" textLength="613" lengthAdjust="spacing">JONAH</text>
    <text class="invite-text" x="58" y="722" font-size="26" textLength="245" lengthAdjust="spacingAndGlyphs">CELEBRATES HIS</text>
    <text class="invite-outline" x="58" y="799" font-size="72" textLength="613" lengthAdjust="spacingAndGlyphs">BAR MITZVAH</text>
    <text class="invite-text" x="58" y="858" font-size="29" textLength="613" lengthAdjust="spacingAndGlyphs">SATURDAY, SEPTEMBER TWENTY EIGHTH</text>
    <text class="invite-text" x="58" y="901" font-size="32" textLength="613" lengthAdjust="spacingAndGlyphs">TWO THOUSAND AND THIRTEEN</text>
    <text class="invite-text" x="228" y="940" font-size="27" textLength="443" lengthAdjust="spacingAndGlyphs">TEN THIRTY IN THE MORNING</text>
    <text class="invite-text" x="58" y="990" font-size="26" textLength="613" lengthAdjust="spacingAndGlyphs">CEDAR RIDGE HEBREW CONGREGATION</text>
    <text class="invite-text" x="58" y="1028" font-size="26" textLength="613" lengthAdjust="spacingAndGlyphs">2280 MAPLE GROVE AVENUE, FAIRLANE, VIRGINIA 20950</text>
    <text class="invite-text" x="58" y="1062" font-size="23" textLength="613" lengthAdjust="spacingAndGlyphs">PLEASE JOIN US FOR A KIDDUSH IMMEDIATELY</text>
    <text class="invite-text" x="58" y="1096" font-size="23" textLength="314" lengthAdjust="spacingAndGlyphs">FOLLOWING THE SERVICE</text>
    <text class="hosts" x="58" y="1147" textLength="613" lengthAdjust="spacing">AARON AND MIRIAM HALE</text>
  </g>
</svg>
</div>
</body>
</html>
```